Colorful Live Music Concert Poster for Paper Lanterns

Looking for a portrait oriented "poster" promoting the band's upcoming show at Marlow Lounge on Sunday, 3/22 at 8 pm, and social version (square format for Instagram). <br/><br/>Copy:<br/>Paper Lanterns<br/>with The Quiet Tides<br/><br/>Marlow Lounge <br/>Sunday, March 22<br/>8 pm<br/><br/>Poster must be consistent with band's overall branding seen on www.paperlanternsmusic.example and it's Streamline page at https://music.example.net/artist/7QwErTy2uIoPaSdFgHjKl?si=123abcDEFghiJKLmnoPQrs <br/><br/>BUT, we wouldn't mind taking in a slightly updated direction. A good example is the cover for our recent single Blue Hours, which is consistent in theme and color palette while updating the design and color at the same time. <br/><br/>The attached files include some band logo art as well as examples of posters done for prior shows. <br/><br/>The posters need not include photos of the band, but if you are so inclined, we've uploaded some selects as well.<br/><br/>Thank you. <br/><br/>Martin<br/>Paper Lanterns

```html
<!DOCTYPE html>
<html lang="en">
<head>
<meta charset="utf-8">
<title>Paper Lanterns with The Quiet Tides – Marlow Lounge</title>
<link rel="stylesheet" href="https://fonts.googleapis.com/css2?family=Josefin+Sans:wght@300;400&family=Kaushan+Script&family=Oswald:wght@600&family=Roboto+Slab:wght@700;900&display=swap">
<style>
  :root {
    --page: #e9e9e9;
    --teal-top: #0fbfc6;
    --teal: #0e8f9a;
    --green: #35b46a;
    --lime: #8cc83a;
    --yellow: #f0d21a;
    --orange: #e98a1a;
    --mint: rgba(220, 248, 236, 0.85);
    --ink: #1c1c1c;
    --band-green: #137a1f;
    --frame-teal: #1497a3;
    --tag-yellow: #f5e21c;
  }
  * { box-sizing: border-box; margin: 0; padding: 0; }
  html, body { width: 1200px; height: 1200px; overflow: hidden; }
  body { background: var(--page); position: relative; }

  .poster {
    position: absolute; left: 275px; top: 140px;
    width: 650px; height: 919px; overflow: hidden;
    background: linear-gradient(180deg, var(--teal-top) 0%, var(--teal) 12%, var(--green) 38%, var(--lime) 60%, var(--yellow) 78%, var(--orange) 100%);
    box-shadow: 0 12px 30px rgba(0,0,0,.25);
    text-align: center;
  }
  .poster-frame {
    position: absolute; inset: 0;
    border: 14px solid transparent;
    border-image: linear-gradient(180deg, #0c6e78, #1d8f62 55%, #c99a1a 85%, #cf7a18) 1;
    opacity: .7; pointer-events: none; z-index: 5;
  }
  .crowd-photo {
    position: absolute; left: 0; right: 0; top: 660px; bottom: 0;
    background: linear-gradient(180deg, rgba(240,200,30,0) 0%, rgba(240,180,30,.7) 25%, #e9a021 60%, #d9761a 100%);
  }
  .band-name {
    position: absolute; top: 24px; left: 0; right: 0;
    font-family: 'Josefin Sans', sans-serif; font-weight: 300;
    color: #fff; font-size: 38px; line-height: 40px; letter-spacing: 4px;
  }
  .with {
    position: absolute; top: 112px; left: 0; right: 0;
    font-family: 'Kaushan Script', cursive; color: #fff; font-size: 26px;
  }
  .support-act, .venue {
    position: absolute; left: 0; right: 0;
    font-family: 'Oswald', sans-serif; font-weight: 600;
    color: var(--mint); text-transform: uppercase; line-height: 1;
    white-space: nowrap;
    text-shadow: 3px 3px 0 rgba(255,255,255,.35);
  }
  .support-act { top: 150px; font-size: 74px; letter-spacing: -1px; }
  .venue {
    top: 236px; font-size: 80px; letter-spacing: -1px;
    transform: scaleY(1.4); transform-origin: top center;
  }

  .date-ribbon { position: absolute; left: 88px; top: 366px; }
  .date-text {
    position: absolute; left: 146px; top: 368px; width: 356px; height: 50px;
    font-family: 'Roboto Slab', serif; font-weight: 900; color: var(--ink);
    font-size: 34px; line-height: 50px; white-space: nowrap;
  }
  .time-tag {
    position: absolute; left: 207px; top: 445px; width: 229px; height: 42px;
    background: var(--tag-yellow); transform: rotate(-2deg);
    font-family: 'Roboto Slab', serif; font-weight: 900; color: var(--ink);
    font-size: 25px; line-height: 44px; z-index: 3;
    box-shadow: 0 2px 4px rgba(0,0,0,.15);
  }
  .time-tag b { font-size: 30px; }

  .snapshots { position: absolute; left: 0; top: 0; }
  .snapshot {
    position: absolute; background: var(--frame-teal);
    padding: 8px 7px 30px; box-shadow: 0 3px 6px rgba(0,0,0,.25);
  }
  .snapshot .photo { width: 100%; height: 100%; border: 1px solid #dfe; }
  .snap-1 { left: 64px; top: 478px; width: 130px; height: 155px; transform: rotate(2deg); }
  .snap-2 { left: 197px; top: 484px; width: 126px; height: 152px; }
  .snap-3 { left: 328px; top: 484px; width: 126px; height: 152px; }
  .snap-4 { left: 460px; top: 480px; width: 127px; height: 155px; }
  .snap-1 .photo { background: linear-gradient(160deg, #cfe2e8, #a45a5a 60%, #e3b75a); }
  .snap-2 .photo { background: linear-gradient(160deg, #b9816a, #d8b79a 45%, #3a3f4a); }
  .snap-3 .photo { background: linear-gradient(160deg, #c8dff0, #9cb27a 55%, #2d2f36); }
  .snap-4 .photo { background: linear-gradient(160deg, #d86f7e, #e5cfc2 50%, #2a2a2a); }

  .address {
    position: absolute; top: 645px; left: 0; right: 0;
    font-family: 'Roboto Slab', serif; font-weight: 700; color: var(--ink);
    font-size: 13px; letter-spacing: .5px;
  }
  .web-band {
    position: absolute; left: 79px; top: 778px; width: 497px; height: 52px;
    background: var(--band-green); transform: rotate(-3deg);
    font-family: 'Roboto Slab', serif; font-weight: 900; color: #fff;
    font-size: 26px; line-height: 54px; opacity: .95; z-index: 3; white-space: nowrap;
  }
  .listen-band {
    position: absolute; left: 150px; top: 824px; width: 345px; height: 34px;
    background: var(--band-green); transform: rotate(-3deg);
    font-family: 'Roboto Slab', serif; font-weight: 700; color: #fff;
    font-size: 12px; line-height: 34px; opacity: .92; z-index: 2; white-space: nowrap;
  }
</style>
</head>
<body>
  <main class="poster">
    <div class="crowd-photo" role="img" aria-label="Crowd of concert fans raising their hands in clouds of yellow and orange colour powder"></div>

    <h1 class="band-name">PAPER<br>LANTERNS</h1>
    <p class="with">with</p>
    <h2 class="support-act">The Quiet Tides</h2>
    <h2 class="venue">Marlow Lounge</h2>

    <svg class="date-ribbon" width="476" height="72" viewBox="0 0 476 72" aria-hidden="true">
      <g fill="none" stroke="#1c1c1c" stroke-width="2">
        <polyline points="58,30 0,30 30,50 0,68 104,68 104,60"/>
        <polyline points="418,30 476,30 446,50 476,68 372,68 372,60"/>
        <rect x="58" y="2" width="360" height="52"/>
      </g>
      <g stroke="#1c1c1c" stroke-width="1.5">
        <line x1="68" y1="56" x2="68" y2="66"/><line x1="74" y1="56" x2="74" y2="66"/>
        <line x1="80" y1="56" x2="80" y2="66"/><line x1="86" y1="56" x2="86" y2="66"/>
        <line x1="92" y1="56" x2="92" y2="66"/><line x1="98" y1="56" x2="98" y2="66"/>
        <line x1="378" y1="56" x2="378" y2="66"/><line x1="384" y1="56" x2="384" y2="66"/>
        <line x1="390" y1="56" x2="390" y2="66"/><line x1="396" y1="56" x2="396" y2="66"/>
        <line x1="402" y1="56" x2="402" y2="66"/><line x1="408" y1="56" x2="408" y2="66"/>
      </g>
    </svg>
    <p class="date-text">MARCH 22, 2020</p>

    <p class="time-tag">TIME: <b>8PM</b></p>

    <div class="snapshots">
      <figure class="snapshot snap-1"><div class="photo" role="img" aria-label="Band duo standing under palm trees"></div></figure>
      <figure class="snapshot snap-2"><div class="photo" role="img" aria-label="Band duo laughing in front of a brick wall"></div></figure>
      <figure class="snapshot snap-3"><div class="photo" role="img" aria-label="Band duo at a seaside fairground"></div></figure>
      <figure class="snapshot snap-4"><div class="photo" role="img" aria-label="Portrait of a band member in front of a colourful wall"></div></figure>
    </div>

    <p class="address">418 Harbor Row, Lakeview, CA&nbsp; 90000</p>

    <p class="web-band">www.paperlanternsmusic.example</p>
    <p class="listen-band">Listen to our EP, Groundwork, on Streamline now!</p>

    <div class="poster-frame"></div>
  </main>
</body>
</html>
```